Business Card Design

WE are looking for a premium quality Business Cards for a Law Firm . Copies of our current business card is attached.
Updates

Went on vacation/holiday

Contact Information for Business Card

xyz

```html
<!DOCTYPE html>
<html lang="en">
<head>
<meta charset="utf-8">
<title>Ashford Lawyers – Business Cards</title>
<link href="https://fonts.googleapis.com/css2?family=Cinzel:wght@600;700&family=Arimo:wght@400;700&display=swap" rel="stylesheet">
<style>
  :root {
    --backdrop: #e6e6e3;
    --paper: #ffffff;
    --green: #0f3b26;
    --gold: #c1995a;
    --ink: #1b2a22;
    --white: #ffffff;
  }
  html, body {
    margin: 0;
    padding: 0;
    width: 1200px;
    height: 960px;
    overflow: hidden;
    background: var(--backdrop);
  }
  .canvas {
    position: relative;
    width: 1200px;
    height: 960px;
  }
  .card {
    position: absolute;
    left: 220px;
    width: 760px;
    height: 434px;
    background: var(--paper);
    border-radius: 30px;
    overflow: hidden;
    box-shadow: 0 10px 28px rgba(0,0,0,0.18);
  }
  .card--offices { top: 22px; }
  .card--profile { top: 504px; }

  /* brand lockup */
  .brand {
    display: flex;
    align-items: center;
    gap: 16px;
    font-family: "Cinzel", serif;
    font-weight: 700;
    color: var(--green);
    letter-spacing: 1px;
    line-height: 1.05;
  }
  .brand__dot {
    flex: none;
    border: 3px solid var(--gold);
    border-radius: 50%;
  }
  .brand__name span { display: block; }

  .card--offices .brand {
    position: absolute;
    top: 70px;
    left: 50%;
    transform: translateX(-50%);
    font-size: 40px;
  }
  .card--offices .brand__dot { width: 62px; height: 62px; }

  .offices {
    position: absolute;
    left: 40px;
    right: 40px;
    top: 230px;
    display: flex;
    justify-content: space-between;
    font-family: "Arimo", sans-serif;
    color: var(--ink);
    font-size: 15px;
    line-height: 1.32;
    text-align: center;
  }
  .office {
    flex: 1;
    padding: 4px 10px;
  }
  .office + .office { border-left: 2px solid var(--gold); }
  .office__city { font-weight: 700; font-size: 16px; margin-bottom: 2px; }
  .office__phone b { font-weight: 700; }

  /* profile card */
  .profile-art {
    position: absolute;
    inset: 0;
  }
  .card--profile .brand {
    position: absolute;
    top: 80px;
    left: 70px;
    font-size: 42px;
  }
  .card--profile .brand__dot { width: 66px; height: 66px; }

  .details {
    position: absolute;
    right: 24px;
    top: 178px;
    text-align: right;
    font-family: "Arimo", sans-serif;
    color: var(--white);
  }
  .details__name {
    font-family: "Cinzel", serif;
    font-weight: 700;
    color: var(--gold);
    font-size: 22px;
    line-height: 30px;
    letter-spacing: 1px;
    margin: 0;
  }
  .details__role { font-size: 14px; line-height: 18px; margin-bottom: 10px; }
  .details__address { font-size: 16px; line-height: 21px; margin-bottom: 12px; }
  .contact {
    list-style: none;
    margin: 0;
    padding: 0;
    font-size: 16px;
  }
  .contact li {
    display: flex;
    justify-content: flex-end;
    align-items: center;
    gap: 10px;
    line-height: 22px;
  }
  .contact svg { width: 14px; height: 14px; flex: none; }
</style>
</head>
<body>
<main class="canvas">

  <section class="card card--offices" aria-label="Office locations">
    <div class="brand">
      <div class="brand__dot"></div>
      <div class="brand__name"><span>Ashford</span><span>Lawyers</span></div>
    </div>
    <div class="offices">
      <div class="office">
        <div class="office__city">Melbourne</div>
        <div>Level 27, 90 Collins Lane</div>
        <div>Melbourne, VIC 3000</div>
        <div class="office__phone"><b>Phone :</b> +61 03 9000 2755</div>
      </div>
      <div class="office">
        <div class="office__city">Sydney</div>
        <div>Level 15, Marlow Building</div>
        <div>48 Station Street</div>
        <div>Northgate, NSW 2190</div>
        <div class="office__phone"><b>Phone :</b> +61 02 8000 3419</div>
      </div>
      <div class="office">
        <div class="office__city">Perth</div>
        <div>Level 28, Kestrel Tower</div>
        <div>210 Bramwell Terrace</div>
        <div>Perth, WA 6000</div>
        <div class="office__phone"><b>Phone :</b> +61 08 6000 7281</div>
      </div>
    </div>
  </section>

  <section class="card card--profile" aria-label="Personal card">
    <svg class="profile-art" width="760" height="434" viewBox="0 0 760 434">
      <polygon points="694,0 712,0 292,434 266,434" fill="var(--gold)"/>
      <polygon points="724,0 760,0 760,434 306,434" fill="var(--green)"/>
    </svg>
    <div class="brand">
      <div class="brand__dot"></div>
      <div class="brand__name"><span>Ashford</span><span>Lawyers</span></div>
    </div>
    <div class="details">
      <h1 class="details__name">Daniel Marsh</h1>
      <div class="details__role">Director &amp; Principal Solicitor<br>MBA, Juris Doctor</div>
      <div class="details__address">Level 3, Ashford House<br>82 Harlow Terrace<br>Kelso Hill, QLD 4100</div>
      <ul class="contact">
        <li>+61 7 3000 4182
          <svg viewBox="0 0 16 16"><path d="M3 1.5l3 .5 1 3.2-1.7 1.3a8 8 0 0 0 4.2 4.2L10.8 9l3.2 1 .5 3-1.8 1.5C7 14.5 1.5 9 1.5 3.3z" fill="var(--gold)"/></svg>
        </li>
        <li>+61 0400 118 276
          <svg viewBox="0 0 16 16"><rect x="4" y="1" width="8" height="14" rx="1.5" fill="none" stroke="var(--gold)" stroke-width="1.8"/></svg>
        </li>
        <li>daniel@ashfordlawyers.com.au
          <svg viewBox="0 0 16 16"><rect x="1" y="3" width="14" height="10" rx="1" fill="var(--gold)"/><path d="M1.5 3.8L8 9l6.5-5.2" fill="none" stroke="var(--green)" stroke-width="1.3"/></svg>
        </li>
        <li>www.ashfordlawyers.com.au
          <svg viewBox="0 0 16 16"><circle cx="8" cy="8" r="7" fill="var(--gold)"/><path d="M1 8h14M8 1c-3 3.5-3 10.5 0 14M8 1c3 3.5 3 10.5 0 14" fill="none" stroke="var(--green)" stroke-width="1.1"/></svg>
        </li>
      </ul>
    </div>
  </section>

</main>
</body>
</html>
```